Medical Device - Case Study Template

We need a TEMPLATE that we can reuse to write various case studies about the medical equipment solutions we provide. It will be a double sided letter sized with a modern design that conveys a feeling of expertise, innovation and highly personable service AND be consistent with the brand guide. The content will be divided into a few sections:

- Situation (200-250 words)
- Challenge (100-120 words)
- Solution (100-120 words)
- Results (100-120 words)
- Conclusion (100-120 words)

Additionally, there will need to be a call to action, inviting people to send an email for more information and a short "About Valtu" section (approx. 40 words).

For device picture placeholders, feel free to use any random small benchtop medical device.

```html
<!DOCTYPE html>
<html lang="en">
<head>
<meta charset="utf-8">
<title>Medical Device Case Study – Valtu</title>
<link rel="stylesheet" href="https://fonts.googleapis.com/css2?family=Montserrat:wght@300;400;600;700&family=Roboto+Condensed:wght@400&display=swap">
<style>
  :root {
    --navy: #12296a;
    --navy-deep: #0d1f52;
    --orange: #f28a2e;
    --ink: #1b1b1b;
    --body: #3a3a3a;
    --paper: #ffffff;
    --photo-a: #1a3b7a;
    --photo-b: #6f8fb4;
  }
  * { box-sizing: border-box; margin: 0; padding: 0; }
  html, body { width: 783px; height: 1200px; overflow: hidden; background: var(--paper); }
  .page { position: relative; width: 783px; height: 1200px; background: var(--paper); font-family: 'Montserrat', sans-serif; color: var(--ink); }
  .backdrop { position: absolute; inset: 0; }
  .brand { position: absolute; left: 51px; top: 54px; display: flex; align-items: center; gap: 10px; }
  .brand-dot { width: 30px; height: 30px; border-radius: 50%; background: var(--orange); }
  .brand-name { font-size: 30px; font-weight: 400; color: var(--navy); letter-spacing: 1px; }
  .hero { position: absolute; left: 49px; top: 162px; color: #fff; }
  .hero-kicker { font-size: 26px; font-weight: 700; letter-spacing: -0.3px; }
  .hero-title { font-size: 49px; line-height: 1; margin-top: 6px; letter-spacing: -0.5px; }
  .hero-title .light { font-weight: 300; color: var(--orange); }
  .hero-title .bold { font-weight: 700; }
  .hero-rule { position: relative; width: 282px; height: 1px; background: rgba(255,255,255,0.35); margin-top: 16px; }
  .hero-rule::before { content: ""; position: absolute; left: 0; top: -1.5px; width: 38px; height: 4px; background: var(--orange); }
  .hero-sub { font-size: 17px; font-weight: 400; line-height: 24px; margin-top: 30px; }
  .section { position: absolute; width: 316px; }
  .section-head { display: flex; align-items: center; gap: 12px; height: 24px; margin-bottom: 10px; }
  .section-head svg { width: 24px; height: 24px; flex: none; }
  .section-title { font-size: 14.5px; font-weight: 600; text-transform: uppercase; color: var(--ink); }
  .section-title .accent { color: var(--orange); }
  .section p { font-family: 'Roboto Condensed', sans-serif; font-size: 10px; line-height: 13.7px; color: var(--body); text-align: justify; }
  .section p + p { margin-top: 13px; }
  .web { position: absolute; left: 50px; top: 1157px; display: flex; align-items: center; gap: 8px; font-size: 13px; font-weight: 600; }
  .contact { position: absolute; left: 420px; top: 1122px; color: #fff; }
  .contact-line { display: flex; align-items: center; gap: 8px; }
  .contact-phone { font-size: 19px; font-weight: 600; letter-spacing: 0.5px; }
  .contact-mail { font-size: 11.5px; font-weight: 600; margin-top: 6px; }
</style>
</head>
<body>
<main class="page">
  <svg class="backdrop" width="783" height="1200" viewBox="0 0 783 1200" aria-hidden="true">
    <defs>
      <linearGradient id="labPhotoTone" x1="0" y1="0" x2="1" y2="1">
        <stop offset="0" stop-color="var(--photo-a)"/>
        <stop offset="0.55" stop-color="var(--photo-b)"/>
        <stop offset="1" stop-color="#1d3f8a"/>
      </linearGradient>
    </defs>
    <rect x="0" y="129" width="360" height="270" fill="var(--navy)"/>
    <polyline points="0,125 340,125 389,61" fill="none" stroke="var(--orange)" stroke-width="4"/>
    <polyline points="0,400 345,400 390,464" fill="none" stroke="var(--orange)" stroke-width="4"/>
    <polygon points="740,1102 783,1102 783,1200 361,1200 405,1102" fill="var(--orange)"/>
    <rect x="0" y="1192" width="363" height="8" fill="var(--navy-deep)"/>
  </svg>

  <svg style="position:absolute;left:0;top:0" width="783" height="470" viewBox="0 0 783 470" role="img" aria-label="Photo of scientists in lab coats examining test tubes and a microscope in a laboratory">
    <polygon points="391,61 783,61 783,464 392,464 348,402 348,127" fill="url(#labPhotoTone)"/>
  </svg>

  <header class="brand">
    <span class="brand-dot"></span>
    <span class="brand-name">Valtu</span>
  </header>

  <section class="hero">
    <div class="hero-kicker">MEDICAL DEVICE</div>
    <div class="hero-title"><span class="light">CASE</span> <span class="bold">STUDY</span></div>
    <div class="hero-rule"></div>
    <p class="hero-sub">Various case studies about the<br>medical equipment solutions</p>
  </section>

  <section class="section" style="left:50px;top:426px">
    <div class="section-head">
      <svg viewBox="0 0 24 24" fill="none" stroke="var(--orange)" stroke-width="1.4"><circle cx="9" cy="8" r="4"/><circle cx="16" cy="14" r="4"/><path d="M3 21c1-3 3-5 6-5"/></svg>
      <h2 class="section-title">Situation</h2>
    </div>
    <p>This section sets out the context of the project in plain terms. Describe the client, the clinical setting and the daily routine of the team that uses the equipment. Note the number of sites, the patient volume and the devices already in service. Explain what prompted the first contact and which people took part in the early talks. Keep the tone clear and factual so that a reader outside the field can follow the story. Add dates where they help and mention any rules or standards that shaped the work from the start of the project.</p>
    <p>The second paragraph can widen the view. Show how the department worked before the new equipment arrived, what tools staff relied on and where time was lost. A short quote from a clinician or manager adds a human voice. Close with a line that leads the reader toward the main challenge the team faced and why solving it mattered to patients and staff alike.</p>
  </section>

  <section class="section" style="left:50px;top:723px">
    <div class="section-head">
      <svg viewBox="0 0 24 24" fill="none" stroke="var(--orange)" stroke-width="1.4"><rect x="3" y="5" width="18" height="14" rx="1"/><path d="M7 15l4-5 3 3 3-4"/></svg>
      <h2 class="section-title">Challenge</h2>
    </div>
    <p>Describe the core problem in a few direct sentences. It may be slow test results, costly downtime, limited bench space or a device that no longer meets current guidance. State who felt the problem most and how it affected care, budgets or workload. Use numbers wherever you can, such as hours lost each week, error rates or the cost of outside services. Mention any limits the client set, like a fixed budget, a tight timeline or the need to keep the lab running during the change. End by naming the goal the team agreed on before any work began on site.</p>
  </section>

  <section class="section" style="left:50px;top:938px">
    <div class="section-head">
      <svg viewBox="0 0 24 24" fill="none" stroke="var(--orange)" stroke-width="1.4"><path d="M12 3a6 6 0 0 0-3.5 10.9V17h7v-3.1A6 6 0 0 0 12 3z"/><path d="M9.5 20h5"/></svg>
      <h2 class="section-title">Solution</h2>
    </div>
    <p>Explain what was supplied and why it was the right fit. Name the benchtop device, its key features and how it was set up in the existing workflow. Cover the training given to staff, the support plan and any custom settings made for this client. Show how our team stayed close during the rollout, from the first site visit to the final check. A photo of the device in use works well here. Keep the focus on the people involved and on the practical steps that turned the plan into a working daily routine for the whole department.</p>
  </section>

  <section class="section" style="left:422px;top:498px">
    <div class="section-head">
      <svg viewBox="0 0 24 24" fill="none" stroke="var(--orange)" stroke-width="1.4"><rect x="5" y="4" width="14" height="17" rx="1"/><rect x="9" y="2" width="6" height="4"/><path d="M8 15l3 2 5-6"/></svg>
      <h2 class="section-title">Results</h2>
    </div>
    <p>Share the outcome with clear, measurable facts. Compare the numbers before and after the change, such as faster turnaround, fewer repeat tests, lower running costs or more patients seen each day. Include feedback from the staff who use the device and from the managers who approved it. If the client noticed gains you did not plan for, mention them too. Charts or a short list of key figures can make this part easy to scan. Keep each claim honest and tied to data the client is happy to share in public, and note the period over which the results were measured.</p>
  </section>

  <section class="section" style="left:422px;top:744px">
    <div class="section-head">
      <svg viewBox="0 0 24 24" fill="none" stroke="var(--orange)" stroke-width="1.4"><circle cx="5" cy="6" r="2"/><circle cx="5" cy="12" r="2"/><circle cx="5" cy="18" r="2"/><path d="M10 6h11M10 12h11M10 18h11"/></svg>
      <h2 class="section-title">Conclusion</h2>
    </div>
    <p>Sum up the story in a few calm, confident lines. Remind the reader of the starting problem, the solution chosen and the main result. Explain what the client plans next, whether that is a wider rollout, a second site or a new type of test. Add a closing word from the client that shows trust in the partnership. Finish with a gentle invitation for readers facing a similar challenge to get in touch by email, so our specialists can talk through their needs and suggest the equipment and support that would suit their own setting best.</p>
  </section>

  <section class="section" style="left:422px;top:974px">
    <div class="section-head">
      <h2 class="section-title">About <span class="accent">Valtu</span></h2>
    </div>
    <p>Valtu supplies and supports medical equipment for clinics, hospitals and labs. Our specialists help teams choose the right devices, set them up with care and keep them running, with friendly service from the first call onward.</p>
  </section>

  <div class="web">
    <svg width="12" height="12" viewBox="0 0 24 24" fill="none" stroke="var(--orange)" stroke-width="2"><circle cx="12" cy="12" r="10"/><path d="M2 12h20M12 2c3 3 3 17 0 20M12 2c-3 3-3 17 0 20"/></svg>
    <span>www.valtumedtech.com</span>
  </div>

  <div class="contact">
    <div class="contact-line contact-phone">
      <svg width="14" height="14" viewBox="0 0 24 24" fill="var(--navy)"><path d="M6.6 10.8a15 15 0 0 0 6.6 6.6l2.2-2.2a1 1 0 0 1 1-.25 11.4 11.4 0 0 0 3.6.6 1 1 0 0 1 1 1V20a1 1 0 0 1-1 1A17 17 0 0 1 3 4a1 1 0 0 1 1-1h3.5a1 1 0 0 1 1 1c0 1.25.2 2.45.6 3.6a1 1 0 0 1-.25 1z"/></svg>
      <span>012.555.0147</span>
    </div>
    <div class="contact-line contact-mail">
      <svg width="13" height="10" viewBox="0 0 26 20" fill="none" stroke="var(--navy)" stroke-width="2.4"><rect x="1" y="1" width="24" height="18"/><path d="M1 1l12 10L25 1"/></svg>
      <span>hello@valtumedtech.com</span>
    </div>
  </div>
</main>
</body>
</html>
```